Mira Lune Window Decals

I need a design for a full set of shop front of window decals. The window and door combined are approximately 3.3m long by 2.38 meters tall, The glass door to one side (attached is a sketch with dimensions - looking from the outside)

Mira Lune is a beauty and massage therapy center that has a balanced mix of business in terms of male and female clients. The business provides traditional foot massage, body massage, seated neck and shoulder massage and a full range of facial skin care services - its basically a combination of day spa and foot massage center.

The store reception desk and retail displays are directly behind the window so I'd like some vision in but also some degree of screening from the bright sun here in Singapore.

Inclusion of a space for a digital photoframe would allow me to play promotions and product detail to the passing traffic (the shop unit is directly opposite a busy shopping mall

I need the design to really state what services are offered and to look gender neutral to ensure male guests are not alienated.

The overall look should lean towards contemporary/modern styling.

Competition is quite considerable in this location with a 'Velnorita' branded beauty salon occupying the unit directly adjacent on the right side.

The idea is that the decals will be printed and installed to the inside of the glass to extend the life and reduce fading

The name of the Business is currently mira lune, however there is no need to include this in the design as there is a sing box above the window (redesigning that signage/logo will be my next project)

I've included a picture of the existing shop front - its pretty woeful.. we only recently purchased the business and need to make a lot of changes... starting with the window... right

Thanks

Tobin
Updates

Project Deadline Extended
Reason: I have extended the deadline as the invitation was accepted by many designers who have yet to submit initial designs Thanks you all for you hard work and effort

Target Market(s)

Male and Female Asian and Expatriate 25-65 years old professionals

Industry/Entity Type

Beauty Salon

Font styles to use
Serif
Sans Serif

Requirements
Must have
• eye catching, and illustrate what we do do
space for digital photo frame (closest power is to the right)
Should not have
• must not look overly femine

```html
<!DOCTYPE html>
<html lang="en">
<head>
<meta charset="utf-8">
<title>Mira Lune Window Decals</title>
<link rel="stylesheet" href="https://fonts.googleapis.com/css2?family=Anton&family=Jura:wght@500;700&display=swap">
<style>
  :root {
    --canvas: #ffffff;
    --orange: #f7941d;
    --ink: #231f20;
    --panel: #272324;
    --decal: #e4e4e6;
    --red: #ed1c24;
    --rule: #cfcfcf;
    --glass-top: #b9b4a8;
    --glass-mid: #7d7a74;
    --glass-low: #5f5e5c;
  }
  html, body {
    margin: 0;
    padding: 0;
    width: 1200px;
    height: 848px;
    overflow: hidden;
    background: var(--canvas);
  }
  .canvas {
    position: relative;
    width: 1200px;
    height: 848px;
  }
  .header-band {
    position: absolute;
    left: 297px; top: 60px;
    width: 760px; height: 90px;
    background: var(--orange);
  }
  .brand-name {
    position: absolute;
    left: 22px; top: 22px;
    margin: 0;
    font-family: "Jura", sans-serif;
    font-weight: 500;
    font-size: 18px;
    line-height: 21px;
    color: var(--ink);
  }
  .service-line {
    position: absolute;
    left: 0; top: 0;
  }
  .window-rule {
    position: absolute;
    left: 297px; top: 166px;
    width: 760px; height: 1px;
    background: var(--rule);
  }
  .door-view {
    position: absolute;
    left: 297px; top: 168px;
    width: 260px; height: 546px;
    background: linear-gradient(180deg, var(--glass-top) 0%, var(--glass-mid) 55%, var(--glass-low) 100%);
  }
  .decal-panel {
    position: absolute;
    left: 557px; top: 168px;
    width: 500px; height: 546px;
    background: var(--panel);
  }
  .footer-band {
    position: absolute;
    left: 120px; top: 729px;
    width: 937px; height: 73px;
    background: var(--red);
  }
  .decal-word {
    font-family: "Jura", sans-serif;
    font-weight: 700;
    fill: var(--decal);
  }
  .service-text {
    font-family: "Anton", sans-serif;
    fill: var(--ink);
  }
</style>
</head>
<body>
<main class="canvas">
  <header class="header-band">
    <p class="brand-name">mira<br>lune</p>
    <svg class="service-line" width="760" height="90" viewBox="0 0 760 90">
      <text class="service-text" x="290" y="73" font-size="48" textLength="440" lengthAdjust="spacingAndGlyphs">SKINCARE + MASSAGE CENTRE</text>
    </svg>
  </header>

  <div class="window-rule"></div>

  <div class="door-view" role="img" aria-label="Photo of the glass shop door with lobby reflections"></div>

  <section class="decal-panel">
    <svg width="500" height="546" viewBox="0 0 500 546">
      <text class="decal-word" x="38" y="167" font-size="200" textLength="428" lengthAdjust="spacingAndGlyphs">FACE</text>
      <text class="decal-word" x="38" y="339" font-size="200" textLength="428" lengthAdjust="spacingAndGlyphs">BODY</text>
      <text class="decal-word" x="38" y="512" font-size="200" textLength="428" lengthAdjust="spacingAndGlyphs">FEET</text>
    </svg>
  </section>

  <footer class="footer-band"></footer>
</main>
</body>
</html>
```